MES Modul-Struktur grafisch veranschaulichen
Zielgruppe
Wir sind Software-Hersteller. Thema 'MES'. Unsere Kunden sind Produktionsunternehmen.
Mit einem MES (Manufacturing Execution System) werden Produktionsprozesse überwacht, geplant, gesteuert und optimiert. Allgemein geht es darum, die Produktivität zu steigern und Kosten zu minimieren.
Eine MES-Software ist modular strukturiert, so dass der Kunde sich nach Bedarf die einzelnen Funktionsmodule zusammenstellen kann. Unser MES LUMARO 7 MAX besteht z.B. aus folgenden Einzelmodulen:
- BASIS (Basismodul)
- MDE (Maschinendatenerfassung)
- BDE (Betriebsdatenerfassung)
- INST (Instandhaltung)
- ALARM (Alarmierung)
- DOK (Dokumentenmanagement)
- TNT (Traceability)
- PLAN (Feinplanung/Leitstand)
- LOG (Logistik)
- VIS (Visualisierung)
- PEP (Personaleinsatzplanung)
- MPZE (Personalzeiterfassung)
- DNC (Rezepturen/DNC)
- EM (Energiemonitoring)
Aufgabenstellung
Die modulare Struktur und der große Umfang an Modulen ist ein wichtiger Vorteil für unsere Kunden, da Sie nicht so schnell an Grenzen stoßen und sich dann unter Umständen eine weitere Insellösung (extra Software mit extra Datenbank ...) anschaffen müssen.
Wichtig ist, dass die einzelnen Module funktionell ineinandergreifen und alle auf die gleiche Datenbank zugreifen.
Es reicht wenn in der Grafik die Module nur mit er Abkürzung, also z.B. MDE bezeichnet werden. Für den ersten Entwurf können auch Platzhalter genutzt werden.
Der Betrachter sollte aus der Grafik auf den ersten Blick erkennen:
- umfängliches MES
- modular strukturiert
- Funktionsmodule step-by-step erweiterbar
Für die Umsetzung naheliegend wären Puzzle-Steine, Brixo, ... muss aber nicht.

```html
<!DOCTYPE html>
<html lang="de">
<head>
<meta charset="utf-8">
<title>MES – Leistung auf Abruf</title>
<link rel="stylesheet" href="https://fonts.googleapis.com/css2?family=Saira:ital,wght@0,400;1,400&display=swap">
<style>
  :root {
    --steel: #476b8c;
    --steel-dark: #3f6383;
    --paper: #ffffff;
  }
  * { box-sizing: border-box; margin: 0; padding: 0; }
  html, body {
    width: 1200px;
    height: 510px;
    overflow: hidden;
    background: var(--paper);
  }
  .canvas {
    position: relative;
    width: 1200px;
    height: 510px;
    background: var(--paper);
    font-family: "Saira", "Arial", sans-serif;
    color: var(--steel);
  }
  .module-grid {
    position: absolute;
    left: 8px;
    top: 9px;
    display: grid;
    grid-template-columns: repeat(5, 225px);
    grid-auto-rows: 89px;
    column-gap: 13px;
    row-gap: 25px;
  }
  .module {
    position: relative;
    border: 3px solid var(--steel);
    border-radius: 6px;
    background: var(--paper);
  }
  .module__led {
    position: absolute;
    left: 2px;
    top: 14px;
    width: 56px;
    height: 56px;
    border-radius: 50%;
    border: 3px solid var(--steel);
  }
  .module__led::before {
    content: "";
    position: absolute;
    left: -4px;
    top: -3px;
    width: 48px;
    height: 50px;
    border-radius: 50%;
    background: var(--steel-dark);
  }
  .module__label {
    position: absolute;
    left: 78px;
    top: 11px;
    width: 127px;
    height: 63px;
    border: 3px solid var(--steel);
    border-top-width: 6px;
    border-left-width: 6px;
    display: flex;
    align-items: center;
    justify-content: center;
    font-style: italic;
    font-size: 31px;
    letter-spacing: 0.5px;
    line-height: 1;
    white-space: nowrap;
  }
  .module__label--wide { font-size: 29px; letter-spacing: 0; }
  .tagline {
    position: absolute;
    left: 0;
    top: 345px;
    width: 1200px;
    text-align: center;
    font-size: 98px;
    font-weight: 400;
    letter-spacing: 2px;
    line-height: 1;
    white-space: nowrap;
  }
</style>
</head>
<body>
<main class="canvas">
  <section class="module-grid" aria-label="MES-Module">
    <div class="module"><span class="module__led"></span><span class="module__label">BASIS</span></div>
    <div class="module"><span class="module__led"></span><span class="module__label">MDE</span></div>
    <div class="module"><span class="module__led"></span><span class="module__label">BDE</span></div>
    <div class="module"><span class="module__led"></span><span class="module__label">INST</span></div>
    <div class="module"><span class="module__led"></span><span class="module__label module__label--wide">ALARM</span></div>

    <div class="module"><span class="module__led"></span><span class="module__label">DOK</span></div>
    <div class="module"><span class="module__led"></span><span class="module__label">TNT</span></div>
    <div class="module"><span class="module__led"></span><span class="module__label">MES</span></div>
    <div class="module"><span class="module__led"></span><span class="module__label">PLAN</span></div>
    <div class="module"><span class="module__led"></span><span class="module__label">LOG</span></div>

    <div class="module"><span class="module__led"></span><span class="module__label">VIS</span></div>
    <div class="module"><span class="module__led"></span><span class="module__label">EM</span></div>
    <div class="module"><span class="module__led"></span><span class="module__label">MPZE</span></div>
    <div class="module"><span class="module__led"></span><span class="module__label">DNC</span></div>
    <div class="module"><span class="module__led"></span><span class="module__label">PEP</span></div>
  </section>
  <h1 class="tagline">MES - Leistung auf Abruf</h1>
</main>
</body>
</html>
```